Online video and marketing company business cards

Need to get some new business cards designed to fit with our new logo. The cards should be professional, clean and simple.

Cards should have:

Name
Position
2 line address
telephone
mobile
email address
web address

We need to have our logo and if possible say what we do...
ONLINE FILM PRODUCTION & STRATEGY

Marketing

```html
<!DOCTYPE html>
<html lang="en">
<head>
<meta charset="utf-8">
<title>Lumareel TV – Business Cards</title>
<link rel="stylesheet" href="https://fonts.googleapis.com/css2?family=Montserrat:wght@400;500;600;700&display=swap">
<style>
  :root {
    --backdrop: #cfcfcf;
    --blue-light: #2f93c6;
    --blue-mid: #17689f;
    --blue-deep: #0b3f6e;
    --navy: #114f82;
    --sky: #5fb2d9;
    --paper: #f3f3f1;
    --ink: #4a4a4a;
    --white: #ffffff;
  }
  * { box-sizing: border-box; margin: 0; padding: 0; }
  html, body { width: 1200px; height: 823px; overflow: hidden; }
  body {
    background: var(--backdrop);
    font-family: "Montserrat", sans-serif;
    position: relative;
  }
  .card {
    position: absolute;
    top: 262px;
    width: 520px;
    height: 298px;
    box-shadow: 0 10px 24px rgba(0,0,0,0.22);
  }
  /* Front */
  .card-front {
    left: 60px;
    background: radial-gradient(circle at 30% 40%, var(--blue-light) 0%, var(--blue-mid) 45%, var(--blue-deep) 100%);
    color: var(--white);
  }
  .front-brand {
    position: absolute;
    left: 52px;
    top: 82px;
    width: 120px;
    height: 120px;
    border: 10px solid var(--white);
    border-radius: 50%;
  }
  .front-copy {
    position: absolute;
    left: 198px;
    top: 88px;
    line-height: 1.05;
  }
  .front-copy .online { font-size: 19px; font-weight: 400; }
  .front-copy .service { font-size: 26px; font-weight: 600; letter-spacing: 0.2px; }
  .front-copy .service .amp { font-size: 18px; font-weight: 500; }
  .front-copy .web { font-size: 19px; font-weight: 400; color: #b9dcef; margin-top: 2px; }
  /* Back */
  .card-back {
    left: 620px;
    background: var(--paper);
    color: var(--ink);
  }
  .holder {
    position: absolute;
    left: 200px;
    top: 32px;
  }
  .holder .name { font-size: 19px; font-weight: 700; color: var(--navy); letter-spacing: 0.3px; }
  .holder .role { font-size: 14px; font-weight: 400; }
  .back-brand {
    position: absolute;
    left: 54px;
    top: 104px;
    display: flex;
    align-items: center;
    gap: 14px;
  }
  .back-brand .mark {
    width: 62px; height: 62px;
    border-radius: 50%;
    background: var(--sky);
  }
  .back-brand .wordmark {
    font-size: 62px;
    font-weight: 700;
    color: var(--sky);
    letter-spacing: -1px;
    line-height: 1;
  }
  .contact {
    position: absolute;
    left: 180px;
    top: 184px;
    font-size: 14.5px;
    line-height: 1.28;
    list-style: none;
  }
  .contact li { display: flex; align-items: flex-start; gap: 6px; }
  .contact .indent { padding-left: 18px; }
  .contact svg { width: 12px; height: 12px; margin-top: 3px; flex: none; fill: var(--sky); }
  .contact .pair { gap: 6px; }
  .contact .pair span + svg { margin-left: 10px; }
</style>
</head>
<body>
  <section class="card card-front" aria-label="Card front">
    <div class="front-brand" aria-hidden="true"></div>
    <div class="front-copy">
      <p class="online">online</p>
      <p class="service">FILM PRODUCTION</p>
      <p class="service"><span class="amp">&amp;</span>STRATEGY</p>
      <p class="web">lumareel.tv</p>
    </div>
  </section>

  <section class="card card-back" aria-label="Card back">
    <div class="holder">
      <p class="name">CARDHOLDER NAME</p>
      <p class="role">Designation</p>
    </div>
    <div class="back-brand">
      <span class="mark" aria-hidden="true"></span>
      <span class="wordmark">lumareel tv</span>
    </div>
    <ul class="contact">
      <li>
        <svg viewBox="0 0 12 12" aria-hidden="true"><path d="M6 0a4 4 0 0 0-4 4c0 3 4 8 4 8s4-5 4-8a4 4 0 0 0-4-4zm0 5.5A1.5 1.5 0 1 1 6 2.5a1.5 1.5 0 0 1 0 3z"/></svg>
        <span>0101 Sunset Avenue, Suite No. 123,</span>
      </li>
      <li class="indent"><span>Your City, City Code, Your Country</span></li>
      <li class="pair">
        <svg viewBox="0 0 12 12" aria-hidden="true"><circle cx="6" cy="6" r="6"/><path d="M3.5 3h1.6l.6 1.6-.9.7a4 4 0 0 0 1.9 1.9l.7-.9 1.6.6v1.6A5.5 5.5 0 0 1 3.5 3z" fill="#fff"/></svg>
        <span>+012 345 6789</span>
        <svg viewBox="0 0 12 12" aria-hidden="true"><rect x="3" y="0" width="6" height="12" rx="1"/><rect x="4" y="1.5" width="4" height="7.5" fill="#fff"/></svg>
        <span>+012 345 6780</span>
      </li>
      <li>
        <svg viewBox="0 0 12 12" aria-hidden="true"><rect x="0" y="2" width="12" height="8" rx="1"/><path d="M0.8 2.8 6 6.6l5.2-3.8" stroke="#fff" stroke-width="1" fill="none"/></svg>
        <span>cardholder.name@lumareel.tv</span>
      </li>
    </ul>
  </section>
</body>
</html>
```